Report presentation for measurement or inline reports

First page of report. Our inline reporting will come in a maintenance map. We want a modern first page and a real eye-catcher for a new company based in the Netherlands called: PRN Luchtcomfort B.V. We are a service company witch measures, balances and give advices at indoor climate HVAC installations. We would like to see designs that use the color blue. We deliver our services to different buildings: Hospitals, atractions, officebuildings, government buildings, swimming pools and schools. Our website: www.prnlc.nl
Updates

Can you all add the new logo please. The companyname is PRN Luchtcomfort B.V.. In witch format can i retrieve the design?

Industry/Entity Type

It Company

Colors
0255a3
3176b5
85abd2
cedeed
eaf1f7
ffffff

Requirements
Must have
• Projectname; projectplace; Inline or measure report; date; logo; companyname. it must be easy printable so not to much colours.
• The companyname is: PRN Luchtcomfort B.V.. Please add the name. A new logo is updated.
Nice to have
• Maybe some pictures from hvac installations, buildings or measure

```html
<!DOCTYPE html>
<html lang="nl">
<head>
<meta charset="utf-8">
<title>Inline reporting – PRN Luchtcomfort B.V.</title>
<link href="https://fonts.googleapis.com/css2?family=Poppins:wght@400;500&display=swap" rel="stylesheet">
<style>
  :root {
    --blue-dark: #0255a3;
    --blue-mid: #3176b5;
    --blue-light: #85abd2;
    --blue-pale: #cedeed;
    --blue-mist: #eaf1f7;
    --white: #ffffff;
    --ink: #333a44;
    --backdrop: #e4e7eb;
  }
  * { box-sizing: border-box; margin: 0; padding: 0; }
  html, body { width: 1200px; height: 797px; overflow: hidden; }
  body {
    background: var(--backdrop);
    font-family: "Poppins", sans-serif;
    color: var(--ink);
    display: flex;
    align-items: center;
    justify-content: center;
  }
  .cover-page {
    position: relative;
    width: 540px;
    height: 764px;
    background: linear-gradient(160deg, var(--white) 0%, #f3f4f6 100%);
    box-shadow: 0 4px 18px rgba(0,0,0,.12);
  }
  .report-type {
    position: absolute;
    top: 58px; left: 205px;
    font-size: 40px;
    font-weight: 400;
    color: var(--blue-dark);
    letter-spacing: .5px;
  }
  .tile { position: absolute; border-radius: 16px; }
  .tile--photo-office {
    left: 200px; top: 135px; width: 255px; height: 155px;
    border-radius: 20px;
    background: linear-gradient(135deg, #6d84ad 0%, #b7bfd0 45%, #d9b25f 75%, #7b7f86 100%);
  }
  .tile--photo-campus {
    left: 285px; top: 328px; width: 235px; height: 190px;
    border-radius: 20px;
    background: linear-gradient(170deg, #93b3d6 0%, #c8d2da 45%, #8c9398 70%, #6f8a63 100%);
  }
  .tile--accent-right { left: 468px; top: 238px; width: 48px; height: 48px; border-radius: 8px; background: var(--blue-mid); }
  .tile--main { left: 140px; top: 300px; width: 132px; height: 132px; border-radius: 16px; background: var(--blue-dark); }
  .tile--tiny { left: 110px; top: 440px; width: 28px; height: 28px; border-radius: 6px; background: var(--blue-dark); }
  .tile--small { left: 148px; top: 452px; width: 78px; height: 78px; border-radius: 12px; background: var(--blue-dark); }

  .project {
    position: absolute;
    left: 70px; top: 548px;
  }
  .project__name { font-size: 23px; font-weight: 500; color: var(--blue-dark); line-height: 1.2; }
  .project__scope { font-size: 15px; color: var(--blue-dark); }
  .project__meta {
    display: flex; gap: 18px; align-items: stretch;
    margin-top: 10px;
    font-size: 14px; color: var(--ink); line-height: 1.25;
  }
  .project__divider { width: 2px; background: var(--blue-mid); }

  .brand {
    position: absolute; left: 70px; top: 664px;
    display: flex; align-items: center; gap: 8px;
  }
  .brand__mark { width: 20px; height: 20px; background: var(--blue-mid); }
  .brand__name { font-size: 17px; font-weight: 500; color: var(--blue-dark); }
  .address { position: absolute; left: 70px; top: 690px; font-size: 11px; }

  .footer-rule { position: absolute; left: 40px; right: 40px; top: 712px; height: 1px; background: #9aa1aa; }
  .contacts {
    position: absolute; left: 70px; right: 90px; top: 722px;
    display: flex; justify-content: space-between;
    font-size: 8.5px; color: var(--ink);
  }
  .cert-badge {
    position: absolute; right: 40px; top: 720px;
    width: 30px; height: 30px; border-radius: 50%;
    border: 2px solid var(--ink);
  }
</style>
</head>
<body>
  <main class="cover-page">
    <h1 class="report-type">Inline reporting</h1>

    <div class="tile tile--photo-office" role="img" aria-label="Foto van een modern kantoorgebouw met verlichte glazen gevel in de schemering"></div>
    <div class="tile tile--accent-right"></div>
    <div class="tile tile--main"></div>
    <div class="tile tile--tiny"></div>
    <div class="tile tile--small"></div>
    <div class="tile tile--photo-campus" role="img" aria-label="Luchtbeeld van een schoolcampus met hoogbouw en lage vleugels"></div>

    <section class="project">
      <h2 class="project__name">ROC Lindehof Definitief</h2>
      <p class="project__scope">Lucht en waterzijdig inregelen</p>
      <div class="project__meta">
        <div>Projectnummer<br>MI11397</div>
        <div class="project__divider"></div>
        <div>Rapportdatum<br>3-10-2011</div>
      </div>
    </section>

    <div class="brand">
      <span class="brand__mark"></span>
      <span class="brand__name">PRN Luchtcomfort B.V.</span>
    </div>
    <p class="address">Postbus 240 5260 AB Vught</p>

    <div class="footer-rule"></div>
    <div class="contacts">
      <span>Tel: +31 (0) 40 555 0123</span>
      <span>Fax: +31 (0) 40 555 0124</span>
      <span>Mobiel: +31 (0) 6 555 012 34</span>
      <span>E-mail: info@prnlc.nl</span>
    </div>
    <div class="cert-badge"></div>
  </main>
</body>
</html>
```